Designing a brochures for an educational counseling service provider

We would like a 4 sided design on a 11x8.5 paper, half folded. I have including a sample design we did to give you an idea of what we envision but we welcome creativity to make beautiful looking flyers. Text for the flier is included as well as our logo.
- The most important thing is capturing our audience/market. We will be handing these flies to schools, organizations and individual clients.

www.plorvaeducationalconsultants.example

Target Market(s)

We are targeting international students wanting to study in the U.S and Canada.

Industry/Entity Type

Education

Requirements
Must have
• - Clean and clear
• - Our logo should visible and well placed.
• - Could you the pictures of students, libraries and school buildings or you could use the pictures we already have.
Nice to have
• We would like this to match business cards.

```html
<!DOCTYPE html>
<html lang="en">
<head>
<meta charset="utf-8">
<title>Plorva Educational Consultants – Brochure</title>
<link href="https://fonts.googleapis.com/css2?family=Open+Sans:wght@400;600&family=Roboto:wght@300;400&display=swap" rel="stylesheet">
<style>
  :root{
    --bg:#3a3a3c;
    --paper:#ffffff;
    --green:#5fb04a;
    --gold:#e2c576;
    --cream:#f4ecd6;
    --blue:#1f67aa;
    --navy:#0d2f55;
    --orange:#ea6a1f;
    --ink:#333a40;
    --heading:#2e6fb5;
  }
  *{box-sizing:border-box;margin:0;padding:0}
  html,body{width:1200px;height:1200px;overflow:hidden;background:var(--bg)}
  body{position:relative;font-family:"Open Sans",Arial,sans-serif;color:var(--ink)}
  .spread{position:absolute;left:220px;width:760px;height:587px;display:flex;box-shadow:0 6px 18px rgba(0,0,0,.45)}
  .spread--outer{top:8px}
  .spread--inner{top:605px}
  .page{position:relative;width:380px;height:587px;background:var(--paper);overflow:hidden}
  .page svg.art{position:absolute;inset:0;width:100%;height:100%}

  /* back cover */
  .contact{position:absolute;left:160px;top:390px;font-size:8.3px;line-height:1.38;color:#444;font-family:"Roboto",Arial,sans-serif}
  .contact p+p{margin-top:8px}

  /* front cover */
  .brand{position:absolute;left:30px;top:52px;display:flex;align-items:center;gap:7px}
  .brand__dot{width:22px;height:22px;border-radius:50%;background:var(--blue)}
  .brand__name{font-family:"Roboto",Arial,sans-serif;font-weight:400;font-size:22px;color:var(--blue)}
  .services-icons{position:absolute;left:30px;bottom:18px;display:flex;gap:38px}
  .services-icons figure{display:flex;flex-direction:column;align-items:center;gap:3px;font-size:5.5px;color:#666}
  .services-icons svg{width:20px;height:20px}

  /* inner pages */
  h2{font-family:"Roboto",Arial,sans-serif;font-weight:300;color:var(--heading);font-size:20px;line-height:1.05}
  .copy{font-size:7.1px;line-height:1.35}
  .copy p{margin-bottom:7px}
  .inner-left__text{position:absolute;left:66px;top:192px;right:20px}
  .inner-left__services{text-align:right;margin-top:6px}
  .services-intro{margin-left:14px}
  .package-title{font-weight:600;margin-top:8px;margin-left:22px}
  .package{list-style:none;margin-top:4px;margin-left:30px}
  .package li{position:relative;padding-left:10px;margin-bottom:2px}
  .package li::before{content:"";position:absolute;left:1px;top:3px;width:4px;height:4px;border-radius:50%;background:var(--orange)}
  .inner-right__text{position:absolute;left:28px;top:26px;right:22px}
  .inner-right__text h2{font-size:18px;margin-top:6px}
  .inner-right__text p{margin-bottom:5px}
</style>
</head>
<body>

<!-- Outer spread: back cover + front cover -->
<section class="spread spread--outer">
  <article class="page page--back">
    <svg class="art" viewBox="0 0 380 587" aria-hidden="true">
      <defs>
        <linearGradient id="goldFade" x1="0" y1="0" x2="1" y2="0">
          <stop offset="0" stop-color="var(--gold)"/><stop offset="1" stop-color="var(--cream)"/>
        </linearGradient>
        <linearGradient id="blueSweep" x1="0" y1="0" x2="0" y2="1">
          <stop offset="0" stop-color="var(--blue)"/><stop offset="1" stop-color="var(--navy)"/>
        </linearGradient>
      </defs>
      <path d="M84 0 H380 V170 C250 185 135 210 90 290 C82 200 82 100 84 0Z" fill="url(#goldFade)"/>
      <path d="M0 0 H80 C70 300 90 500 250 587 H0Z" fill="var(--green)"/>
      <path d="M80 0 H88 C78 300 100 495 272 587 H250 C90 500 70 300 80 0Z" fill="url(#blueSweep)"/>
    </svg>
    <div class="contact">
      <p>Executive Director &amp; Independent<br>Educational Consultant<br>Plorva Educational Consultants, LLC<br>418 Harlow Road<br>Suite 9B, Ridgefield, TX 75010</p>
      <p>Phone: 555-204-3318<br>Email: mara@plorvaeducationalconsultants.example</p>
    </div>
  </article>

  <article class="page page--front">
    <svg class="art" viewBox="0 0 380 587">
      <defs>
        <linearGradient id="creamFade" x1="0" y1="0" x2="1" y2="1">
          <stop offset="0" stop-color="var(--cream)"/><stop offset="1" stop-color="#ffffff"/>
        </linearGradient>
        <radialGradient id="photoTone" cx="0.55" cy="0.45" r="0.7">
          <stop offset="0" stop-color="#8a5a3e"/><stop offset="0.6" stop-color="#4a2e20"/><stop offset="1" stop-color="#2a1a12"/>
        </radialGradient>
      </defs>
      <rect width="380" height="260" fill="url(#creamFade)"/>
      <ellipse cx="330" cy="300" rx="300" ry="230" transform="rotate(-28 330 300)" fill="var(--blue)"/>
      <ellipse cx="338" cy="292" rx="282" ry="210" transform="rotate(-28 338 292)" fill="url(#photoTone)" role="img" aria-label="Photo of smiling international students"/>
    </svg>
    <div class="brand">
      <span class="brand__dot"></span>
      <span class="brand__name">Plorva</span>
    </div>
    <div class="services-icons">
      <figure>
        <svg viewBox="0 0 20 20" fill="none" stroke="#555" stroke-width="1.2"><path d="M2 7 L10 2 L18 7Z M4 8v8 M8 8v8 M12 8v8 M16 8v8 M2 17h16"/></svg>
        <figcaption>Boarding</figcaption>
      </figure>
      <figure>
        <svg viewBox="0 0 20 20" fill="none" stroke="#555" stroke-width="1.2"><path d="M2 8 L10 4 L18 8 L10 12Z M5 10v4c3 2 7 2 10 0v-4"/></svg>
        <figcaption>Admission</figcaption>
      </figure>
      <figure>
        <svg viewBox="0 0 20 20" fill="none" stroke="#555" stroke-width="1.2"><path d="M3 7h12 M12 4l3 3-3 3 M17 13H5 M8 10l-3 3 3 3"/></svg>
        <figcaption>Transfer</figcaption>
      </figure>
      <figure>
        <svg viewBox="0 0 20 20" fill="none" stroke="#555" stroke-width="1.2"><circle cx="10" cy="8" r="5"/><path d="M7 12l-2 6 5-2 5 2-2-6"/></svg>
        <figcaption>Scholarship</figcaption>
      </figure>
    </div>
  </article>
</section>

<!-- Inner spread -->
<section class="spread spread--inner">
  <article class="page page--inner-left">
    <svg class="art" viewBox="0 0 380 587">
      <defs>
        <linearGradient id="libraryTone" x1="0" y1="0" x2="1" y2="0">
          <stop offset="0" stop-color="#3b2b24"/><stop offset="0.5" stop-color="#8a6450"/><stop offset="1" stop-color="#c9a27a"/>
        </linearGradient>
      </defs>
      <path d="M0 0 H380 V120 C250 130 110 160 40 190 H0Z" fill="url(#libraryTone)" role="img" aria-label="Photo of students studying together in a library"/>
      <path d="M0 108 C20 100 35 98 45 98 C23 300 38 500 143 587 H0Z" fill="var(--blue)"/>
      <path d="M45 98 C23 300 38 500 143 587 H153 C46 500 30 300 52 97Z" fill="var(--orange)"/>
    </svg>
    <div class="inner-left__text copy">
      <h2>About Us:</h2>
      <p>Our mission is to make quality education accessible and affordable to the families we serve. Our services are designed with the child's future in mind. Whether one is seeking an academic or non-academic environment, it is important to us that we set our clients up for success.</p>
      <p>We are a family-centered organization and our goals are the same as those of our clients; for their child to thrive and reach their goals and dreams. With over 10 years of experience in the business, we are aware of the financial obstacles created by the ever increasing cost in education. Our expert consultants work closely with families to map out their educational budget and find the best affordable and quality educational options.</p>
      <h2 class="inner-left__services">Services:</h2>
      <p class="services-intro">Finding the right school or program for your child is one of the most important decisions your family will make. The right choice will make a major impact on your child's future.</p>
      <p class="package-title">Our package includes:</p>
      <ul class="package">
        <li>Intake interview</li>
        <li>Present range of options based on needs and goals of the family</li>
        <li>Interview coaching</li>
        <li>Assistance with application and essays</li>
        <li>Updates on student progress throughout their enrollment with the school</li>
        <li>Advisement on financial documents and visa applications</li>
      </ul>
    </div>
  </article>

  <article class="page page--inner-right">
    <div class="inner-right__text copy">
      <h2>Boarding schools:</h2>
      <p>Students who want the best out of their grade school experience are likely to choose boarding schools because they are proven to better prepare students for university. North American boarding schools provide a quality dynamic experience that will facilitate personal growth in independence, leadership, and confidence as well as provide the academic curriculum necessary to prepare students for university.</p>
      <h2>College admission:</h2>
      <p>As Educational Consultants, we specialize in college/university admissions and we understand how confusing, time-consuming, and stressful the application process can be. Our experienced counselors are here to answer your questions and guide you step by step. As Parents and students may have limited access to information on schools, may not know or understand the entire process as a whole, nor where/how to begin, our experts counselors have solutions.</p>
      <p>Clients increase the odds of admissions with our comprehensive plan of action. We believe that regardless of a student's level of involvement in extra-curricular activities or preparedness, they still possess something they can offer to the university; therefore we help them shine on their college applications.</p>
      <h2>Transfer students:</h2>
      <p>Need to find a school an alternative school that is a better match for you? We work with students and families to transfer from one school to another.</p>
      <h2>Scholarships:</h2>
      <p>Funding the education for your children in some of the world's top schools can be very expensive as tuition and fees increase at an average of 4% every year. We work with you to determine the budget for your family, applying to scholarship available and guide you through the financial aid process.</p>
      <p>Over 70% of our clients have been awarded scholarships or Financial Aid, making your education goals attainable an affordable and your children education possible.</p>
      <p>Our consultants are members of ACEA, the leading association for educational consultants in North America.</p>
    </div>
  </article>
</section>

</body>
</html>
```